Agency Website & Personal brand

My name is Kostas Vranelis & I've been a digital marketer & an e-commerce expert since 2010.

- I've spoken to 20 different events around the world up to 3,000 people in size.
- I've sold over 1500 training courses around e-commerce growth.
- I have over 100 testimonials (video & photo) from successful students who bought my training
- I have dozens of video testimonials from respected entrepreneurs that vouch for me and my work
- I have photos with marketing legends with that I shared the stage like Owen Tarrick, Martin Fellowbrand, Glen Maro & more
- I am the host of the Aegean Roundtable since 2017 - a high-level networking event for 7 & 8 figure entrepreneurs - 100 people have come to Greece since 2017
- I have tons of videos created where I showcase my expertise on growth
- I have worked with dozens of e-commerce stores on their growth & helped them scale to multiple 6, 7 & 8 figures either on consulting

I need a website design that showcases my authority & be a lead generating machine.

The goal is to bring people on a call with me but also grab their email and start building the relationship with them and free valuable content

We have 3 offers :

1. Paid ads (Done for You)
2. Consulting/Mastermind (Done with You)
3. Training (Do it Yourself)

```html
<!DOCTYPE html>
<html lang="en">
<head>
<meta charset="utf-8">
<title>Kostas Vranelis — Digital Agency</title>
<link href="https://fonts.googleapis.com/css2?family=Roboto:wght@400;500;700;900&display=swap" rel="stylesheet">
<style>
:root{
  --blue-deep:#0a3f80;
  --blue:#0f5aa8;
  --blue-light:#4aa8f5;
  --ink:#111;
  --dark:#262626;
  --footer:#2f2f2f;
  --white:#fff;
  --field:#e9e9e9;
  --muted:#333;
}
*{box-sizing:border-box;margin:0;padding:0}
html,body{width:1200px;height:3125px;overflow:hidden}
body{position:relative;font-family:'Roboto',Arial,sans-serif;color:var(--ink);background:var(--white)}
.abs{position:absolute}
.btn{position:absolute;display:flex;align-items:center;justify-content:center;color:var(--white);font-weight:700;font-size:14px;background:linear-gradient(90deg,var(--blue-deep),var(--blue-light));letter-spacing:.2px}

/* hero */
.hero{position:absolute;left:0;top:0;width:1200px;height:598px;background:linear-gradient(90deg,#141d2b 0%,#253247 40%,#4b5b70 70%,#6b7b8e 100%)}
.logo{position:absolute;left:110px;top:26px;color:var(--white);font-weight:700;font-size:22px}
.nav{position:absolute;left:340px;top:32px;display:flex;gap:0;color:var(--white);font-size:11px}
.nav span{position:absolute;white-space:nowrap}
.call{left:898px;top:22px;width:190px;height:41px;font-size:11px;font-weight:400;gap:8px}
.call b{font-weight:700}
.hero h1{position:absolute;left:112px;top:168px;color:var(--white);font-size:40px;line-height:45px;font-weight:700}
.hero p{position:absolute;left:114px;top:285px;width:420px;color:var(--white);font-size:11.5px;line-height:19px}
.hero .btn{left:113px;top:371px;width:153px;height:48px}

/* offers */
.offers{position:absolute;left:0;top:598px;width:1200px;height:442px;background:var(--dark)}
.offers h2{position:absolute;top:36px;width:100%;text-align:center;color:var(--white);font-size:37px;font-weight:700}
.card{position:absolute;top:109px;width:228px;height:273px;background:var(--white);padding:0 24px}
.card .num{position:absolute;right:0;top:0;width:26px;height:26px;background:var(--blue);color:var(--white);font-size:13px;font-weight:700;display:flex;align-items:center;justify-content:center}
.card svg{position:absolute;left:26px;top:24px}
.card h3{position:absolute;left:24px;top:86px;font-size:13.5px;font-weight:500;line-height:18px}
.card p{position:absolute;left:25px;width:180px;font-size:10.5px;line-height:19px;color:var(--muted)}
.card hr{position:absolute;left:25px;top:237px;width:150px;border:0;border-top:1px solid #555}
.card a{position:absolute;left:26px;top:247px;font-size:10.5px;font-weight:700;color:var(--blue-deep);text-decoration:none}

/* about */
.photo{position:absolute}
.tile{position:absolute;width:66px;height:66px;background:linear-gradient(135deg,var(--blue-deep),var(--blue-light));display:flex;align-items:center;justify-content:center}
.dots{position:absolute;left:458px;top:1446px;width:94px;height:128px;background-image:radial-gradient(#222 1.2px,transparent 1.4px);background-size:11px 11px}
.about h2{position:absolute;left:609px;top:1146px;font-size:38px;line-height:46px;font-weight:700}
.about .lead{position:absolute;left:613px;top:1259px;width:495px;font-size:14.5px;line-height:19px;font-weight:700}
.about .body{position:absolute;left:611px;width:500px;font-size:11px;line-height:19px;color:var(--muted)}
.about .btn{left:615px;top:1519px;width:153px;height:47px}

/* focus */
.focus-title{position:absolute;top:1615px;left:0;width:1172px;text-align:center;font-size:37px;font-weight:700}
.band{position:absolute;left:0;top:1890px;width:1200px;height:352px;background:#141414}
.frame{position:absolute;left:189px;top:1674px;width:821px;height:220px;border:2px solid var(--blue);border-bottom:0}
.video{position:absolute;left:203px;top:1687px;width:795px;height:373px;background:linear-gradient(180deg,#dcdcdc 0%,#cfd2d4 45%,#48546a 75%,#2a2f3a 100%)}
.play{position:absolute;left:546px;top:1830px;width:108px;height:87px;background:rgba(35,90,150,.9);display:flex;align-items:center;justify-content:center}

/* features */
.features{position:absolute;left:113px;top:2111px;width:974px;height:227px;background:linear-gradient(90deg,var(--blue-deep) 0%,#1561b0 55%,var(--blue-light) 100%);color:var(--white)}
.features h2{position:absolute;left:48px;top:70px;font-size:38px;line-height:44px;font-weight:700}
.stat{position:absolute;top:40px;width:160px;text-align:center}
.stat svg{display:block;margin:0 auto}
.stat strong{display:block;font-size:38px;line-height:44px;font-weight:700;margin-top:2px}
.stat span{display:block;font-size:14px;line-height:19px;font-weight:500}

/* contact */
.contact-info h2{position:absolute;left:110px;top:2402px;font-size:29px;font-weight:700}
.contact-info p{position:absolute;left:113px;top:2450px;font-size:11px}
.info-row{position:absolute;left:118px;display:flex;align-items:center;gap:18px;font-size:15px}
.info-row i{width:38px;height:38px;background:var(--blue-deep);display:flex;align-items:center;justify-content:center}
.form{position:absolute;left:671px;top:2398px;width:416px;height:322px;background:var(--white);box-shadow:0 0 18px rgba(0,0,0,.12)}
.form h2{position:absolute;top:8px;width:100%;text-align:center;font-size:38px;font-weight:900}
.field{position:absolute;left:41px;width:325px;height:32px;background:var(--field);font-size:11.5px;padding:10px 14px;color:#222}
.form .btn{left:41px;top:268px;width:128px;height:37px;background:var(--blue-deep)}

/* footer */
.footer{position:absolute;left:0;top:2778px;width:1200px;height:347px;background:var(--footer);color:var(--white)}
.footer h4{position:absolute;font-size:18px;font-weight:500}
.footer .about-text{position:absolute;left:112px;top:97px;width:200px;font-size:11px;line-height:23px}
.footer ul{position:absolute;list-style:none;font-size:14.5px}
.social{position:absolute;left:112px;top:199px;display:flex;gap:18px}
.social span{width:26px;height:26px;border-radius:50%;background:var(--white)}
.news-field{position:absolute;left:824px;top:98px;width:263px;height:44px;background:var(--white);color:#222;font-size:15px;padding:12px 20px}
.footer .btn{left:824px;top:162px;width:148px;height:45px;font-size:17px}
.footer .rule{position:absolute;left:0;top:300px;width:1200px;border-top:1px solid #555}
.footer .copy{position:absolute;top:315px;width:1205px;text-align:center;font-size:15px}
</style>
</head>
<body>

<header class="hero" role="img" aria-label="Photo of three colleagues working together at an office desk">
  <div class="logo">KOSTAS VRANELIS</div>
  <nav class="nav">
    <span style="left:0">Introduction</span>
    <span style="left:90px">About Us</span>
    <span style="left:164px">Welcome Message</span>
    <span style="left:284px">Our Services</span>
    <span style="left:379px">Our Team</span>
    <span style="left:459px">Contact Us</span>
  </nav>
  <div class="btn call">
    <svg width="16" height="16" viewBox="0 0 16 16"><circle cx="8" cy="8" r="8" fill="#fff"/><path d="M5.2 4.2l1.4-.3.8 2-1 .8c.5 1.1 1.3 1.9 2.4 2.4l.8-1 2 .8-.3 1.4c-3.4.2-6.3-2.7-6.1-6.1z" fill="#0f5aa8"/></svg>
    <span><b>CALL NOW;</b> +1 555 014 2290</span>
  </div>
  <h1>DIGITAL AGENCY FOR<br>YOUR BUSINESS</h1>
  <p>Lorem Ipsum is simply dummy text of the printing and typesetting industry. Lorem Ipsum has been the industry's standard dummy text ever since the 1500s, when an unknown printer took a galley of type and scrambled it to make a type</p>
  <div class="btn">GET STARTED</div>
</header>

<section class="offers">
  <h2>WHAT WE OFFER</h2>
  <article class="card" style="left:235px">
    <div class="num">01</div>
    <svg width="52" height="50" viewBox="0 0 52 50" fill="none" stroke="#0f5aa8" stroke-width="1.6"><rect x="2" y="6" width="42" height="40" rx="2"/><line x1="2" y1="14" x2="44" y2="14"/><rect x="9" y="20" width="26" height="12"/><text x="13" y="30" font-size="9" fill="#0f5aa8" stroke="none" font-family="Roboto,sans-serif">Ads</text><line x1="9" y1="38" x2="35" y2="38"/><circle cx="44" cy="8" r="6"/></svg>
    <h3>PAID ADS (DONE FOR YOU)</h3>
    <p style="top:112px">Lorem Ipsum is simply dummy text of the printing and typesetting industry. Lorem Ipsum has been the industry's standard dummy text ever since the 1500s, when an unknown printer took a galley of</p>
    <hr><a>Read More....</a>
  </article>
  <article class="card" style="left:484px">
    <div class="num">02</div>
    <svg width="52" height="50" viewBox="0 0 52 50" fill="none" stroke="#0f5aa8" stroke-width="1.6"><rect x="14" y="4" width="34" height="24"/><line x1="20" y1="12" x2="42" y2="12"/><line x1="20" y1="18" x2="36" y2="18"/><circle cx="8" cy="18" r="4"/><path d="M3 46V28h10l8-6"/><line x1="31" y1="28" x2="31" y2="46"/></svg>
    <h3 style="left:22px">TRAINING (DO IT YOURSELF)</h3>
    <p style="top:112px">Lorem Ipsum is simply dummy text of the printing and typesetting industry. Lorem Ipsum has been the industry's standard dummy text ever since the 1500s, when an unknown printer took a galley of</p>
    <hr><a>Read More....</a>
  </article>
  <article class="card" style="left:734px">
    <div class="num">03</div>
    <svg width="52" height="50" viewBox="0 0 52 50" fill="none" stroke="#0f5aa8" stroke-width="1.6"><rect x="16" y="2" width="20" height="14" rx="2"/><circle cx="10" cy="22" r="4"/><circle cx="42" cy="22" r="4"/><circle cx="26" cy="22" r="4"/><rect x="4" y="30" width="44" height="6"/><line x1="10" y1="36" x2="10" y2="48"/><line x1="42" y1="36" x2="42" y2="48"/></svg>
    <h3 style="left:24px">CONSULTING/MASTERMIND<br>(DONE WITH YOU)</h3>
    <p style="top:128px">Lorem Ipsum is simply dummy text of the printing and typesetting industry. Lorem Ipsum has been the industry's standard dummy text ever since the 1500s, when an</p>
    <hr><a>Read More....</a>
  </article>
</section>

<section class="about">
  <div class="photo" style="left:133px;top:1305px;width:325px;height:278px;background:linear-gradient(135deg,#c9a77f,#8a6a4a 60%,#3b3b3b)" role="img" aria-label="Photo of hands typing on a laptop"></div>
  <div class="photo" style="left:227px;top:1112px;width:325px;height:331px;background:linear-gradient(160deg,#a8824f,#6a5136 50%,#3a3a3f)" role="img" aria-label="Photo of two smiling men posing together"></div>
  <div class="dots"></div>
  <div class="tile" style="left:199px;top:1088px">
    <svg width="34" height="34" viewBox="0 0 34 34" fill="none" stroke="#fff" stroke-width="1.6"><path d="M12 22c-3-2-5-5-5-9a10 10 0 0 1 20 0c0 4-2 7-5 9v4H12z"/><line x1="13" y1="30" x2="21" y2="30"/></svg>
  </div>
  <div class="tile" style="left:97px;top:1542px">
    <svg width="36" height="36" viewBox="0 0 36 36" fill="none" stroke="#fff" stroke-width="1.6"><path d="M14 22l-4-4c4-9 12-14 22-14 0 10-5 18-14 22z"/><circle cx="22" cy="14" r="3"/><path d="M10 18l-5 1 4-6h5M18 26l-1 5 6-4v-5"/><path d="M9 27l-4 4"/></svg>
  </div>
  <h2>LEADING THE BEST DIGITAL<br>AGENCY IN TOWN</h2>
  <p class="lead">We provide Digital Signage, Sound solutions and Scan &amp; Go for retail and public places. With knowledge and extensive experience we deliver solutions that creates customer value and customer experience.</p>
  <p class="body" style="top:1339px">Lorem Ipsum is simply dummy text of the printing and typesetting industry. Lorem Ipsum has been the industry's standard dummy text ever since the 1500s, when an unknown printer took a galley of type and scrambled it to make a type specimen book. It has survived not only five centuries, but also the leap into electronic typesetting,</p>
  <p class="body" style="top:1432px">remaining essentially unchanged. It was popularised in the 1960s with the release of Letraset sheets containing Lorem Ipsum passages, and more recently with desktop publishing software like Aldus PageMaker including versions of Lorem Ipsum.</p>
  <div class="btn">LEARN MORE</div>
</section>

<section class="focus">
  <h2 class="focus-title">OUR FOCUS AREAS</h2>
  <div class="band"></div>
  <div class="frame"></div>
  <div class="video" role="img" aria-label="Video still of two men talking in a studio interview setup"></div>
  <div class="play"><svg width="36" height="40" viewBox="0 0 36 40"><path d="M4 2l30 18L4 38z" fill="#fff"/></svg></div>
</section>

<section class="features">
  <h2>OUR<br>FEATURE</h2>
  <div class="stat" style="left:238px">
    <svg width="56" height="54" viewBox="0 0 56 54" fill="none" stroke="#fff" stroke-width="1.6"><rect x="6" y="14" width="44" height="32"/><rect x="12" y="26" width="6" height="20"/><rect x="24" y="20" width="6" height="26"/><rect x="36" y="30" width="6" height="16"/><line x1="2" y1="48" x2="54" y2="48"/></svg>
    <strong>20</strong><span>DIFFERENT<br>EVENTS</span>
  </div>
  <div class="stat" style="left:417px">
    <svg width="56" height="54" viewBox="0 0 56 54" fill="none" stroke="#fff" stroke-width="1.6"><rect x="4" y="6" width="48" height="32"/><path d="M10 16l10 8 10-8"/><rect x="34" y="14" width="12" height="14"/><line x1="20" y1="46" x2="36" y2="46"/><line x1="28" y1="38" x2="28" y2="46"/></svg>
    <strong>3,000</strong><span>PEOPLE AROUND<br>THE WORLD</span>
  </div>
  <div class="stat" style="left:606px">
    <svg width="56" height="54" viewBox="0 0 56 54" fill="none" stroke="#fff" stroke-width="1.6"><rect x="4" y="4" width="48" height="34"/><line x1="4" y1="12" x2="52" y2="12"/><rect x="32" y="20" width="4" height="12"/><rect x="40" y="16" width="4" height="16"/><path d="M10 30l8-10 6 6"/><line x1="28" y1="38" x2="28" y2="48"/><line x1="18" y1="48" x2="38" y2="48"/></svg>
    <strong>1500</strong><span>TRAINING<br>COURSES</span>
  </div>
  <div class="stat" style="left:784px">
    <svg width="56" height="54" viewBox="0 0 56 54" fill="none" stroke="#fff" stroke-width="1.6"><rect x="4" y="16" width="48" height="26"/><rect x="30" y="4" width="18" height="24"/><path d="M36 12l6 4-6 4z"/><path d="M10 12l12 12"/><line x1="28" y1="42" x2="28" y2="50"/><line x1="18" y1="50" x2="38" y2="50"/></svg>
    <strong>100</strong><span>TESTIMONIALS<br>FROM SUCCESSFUL<br>STUDENTS</span>
  </div>
</section>

<section class="contact-info">
  <h2>CONTACT INFORMATION</h2>
  <p>Please contact us on phone or email. You find the contact information below.</p>
  <div class="info-row" style="top:2494px">
    <i><svg width="16" height="20" viewBox="0 0 16 20"><path d="M8 0a7 7 0 0 1 7 7c0 5-7 13-7 13S1 12 1 7a7 7 0 0 1 7-7z" fill="#fff"/><circle cx="8" cy="7" r="2.6" fill="#0a3f80"/></svg></i>
    <span><b>Address</b>;Lorem Ipsum is simply</span>
  </div>
  <div class="info-row" style="top:2569px">
    <i><svg width="26" height="18" viewBox="0 0 26 18" fill="none" stroke="#fff" stroke-width="1.6"><rect x="1" y="1" width="24" height="16"/><path d="M1 1l12 9 12-9M1 17l9-8M25 17l-9-8"/></svg></i>
    <span><b>Mail:</b> hello@vranelisgrowth.com</span>
  </div>
  <div class="info-row" style="top:2636px">
    <i><svg width="20" height="20" viewBox="0 0 20 20"><path d="M3 1l4-1 2 5-2.5 2c1.2 2.6 3.1 4.5 5.5 5.5l2-2.5 5 2-1 4C9 17 3 11 3 1z" fill="#fff"/></svg></i>
    <span><b>Phone:</b> 555 018 4420</span>
  </div>
</section>

<section class="form">
  <h2>CONTACT US</h2>
  <div class="field" style="top:55px">NAME</div>
  <div class="field" style="top:100px">EMAIL</div>
  <div class="field" style="top:144px">PHONE</div>
  <div class="field" style="top:189px;height:65px">MESSAGE</div>
  <div class="btn">SUBMIT</div>
</section>

<footer class="footer">
  <h4 style="left:111px;top:67px">KOSTAS VRANELIS</h4>
  <p class="about-text">Lorem Ipsum is simply dummy text of the printing and typesetting industry. Lorem Ipsum has been the industry's standard dummy text ever since the</p>
  <div class="social" aria-label="Social links"><span></span><span></span><span></span><span></span></div>
  <h4 style="left:364px;top:67px">SERVICES</h4>
  <ul style="left:364px;top:98px;line-height:37.5px"><li>Copywriting</li><li>Email Marketing</li><li>Digital Advertising</li><li>Social Media Marketing</li></ul>
  <h4 style="left:612px;top:70px">COMPANY</h4>
  <ul style="left:614px;top:100px;line-height:30.5px"><li>Who we are</li><li>Careers</li><li>Cilent reviews</li><li>Contact</li><li>Blog</li></ul>
  <h4 style="left:824px;top:70px">NEWSLETTER</h4>
  <div class="news-field">EMAIL</div>
  <div class="btn">SUBSCRIBE</div>
  <div class="rule"></div>
  <p class="copy">Copyright © 2023 vranelisgrowth.com</p>
</footer>

</body>
</html>
```